Brightway Haul & Repair Services, are a company that offers a 'one stop shop' pre-move clean up a

I have already selected a logo which I would like on the front of the business cards along with phone numbers, web address and email which are:
0419574302
www.brightwayhaul.com.au
brightwayhaulrepair@mailbox.example

On the back of the card I would like to list some of the types of service we offer (clean - move - repairs/maintenance) which are:
CLEAN - windows, gutters, solar panels, driveways/paths, carpets.
MOVE - Small/medium size house/office moves, large item pick-up & delivery, yard clean-up and removal.
General maintenance and repairs.

I would like the blue logo on a gray background.

Thanks

```html
<!DOCTYPE html>
<html lang="en">
<head>
<meta charset="utf-8">
<title>Brightway Haul &amp; Repair Services – Business Cards</title>
<link rel="stylesheet" href="https://fonts.googleapis.com/css2?family=Open+Sans:wght@400;600;700;800&display=swap">
<style>
  :root {
    --backdrop: #2a2a2a;
    --brand-blue: #1f6db8;
    --brand-blue-light: #5aa9e6;
    --card-white: #ffffff;
    --card-black: #050505;
    --ink-dark: #1a1a1a;
    --ink-light: #e8e8e8;
  }
  * { box-sizing: border-box; margin: 0; padding: 0; }
  html, body {
    width: 1200px; height: 900px; overflow: hidden;
    background: var(--backdrop);
    font-family: "Open Sans", sans-serif;
  }
  .canvas { position: relative; width: 1200px; height: 900px; }

  .card {
    position: absolute;
    width: 540px; height: 310px;
    overflow: hidden;
    box-shadow: 0 18px 40px rgba(0,0,0,.55);
  }

  /* Services side */
  .card--services { left: 60px; top: 110px; background: var(--card-white); }
  .services-band { position: absolute; inset: 0; width: 100%; height: 100%; }
  .services-name {
    position: absolute; left: 30px; top: 104px;
    font-size: 28px; font-weight: 800; letter-spacing: .5px;
    text-transform: uppercase; color: var(--card-white);
    white-space: nowrap;
  }
  .services-list {
    position: absolute; left: 30px; top: 178px; width: 480px;
    font-size: 13.5px; line-height: 1.6; color: var(--ink-dark);
  }
  .services-list strong { font-weight: 700; }
  .services-list .services-extra { color: var(--brand-blue-light); font-weight: 600; font-size: 15px; }

  /* Contact side */
  .card--contact { left: 600px; top: 480px; background: var(--card-black); }
  .contact-name {
    position: absolute; right: 36px; top: 54px; width: 320px; text-align: right;
    font-size: 24px; font-weight: 800; line-height: 1.15; color: var(--brand-blue);
  }
  .contact-list {
    position: absolute; right: 36px; top: 140px;
    list-style: none; text-align: right;
  }
  .contact-item {
    display: flex; justify-content: flex-end; align-items: center; gap: 10px;
    font-size: 15px; line-height: 1.65; color: var(--ink-light);
  }
  .contact-item--web { color: var(--brand-blue-light); font-size: 16px; }
  .contact-icon { width: 14px; height: 14px; fill: var(--brand-blue-light); flex: none; }
  .contact-stripe {
    position: absolute; left: 0; right: 0; bottom: 22px; height: 14px;
    background: var(--brand-blue);
  }
</style>
</head>
<body>
<main class="canvas">

  <section class="card card--services" aria-label="Services side">
    <svg class="services-band" viewBox="0 0 540 310" preserveAspectRatio="none" aria-hidden="true">
      <polygon points="0,0 540,0 540,60 440,60 410,150 0,150" fill="var(--brand-blue)"/>
    </svg>
    <p class="services-name">Brightway Haul</p>
    <p class="services-list">
      <strong>CLEAN</strong> - windows, gutters, solar panels, driveways/paths, carpets.<br>
      <strong>MOVE</strong> - Small/medium size house/office moves, large item pick-up &amp; delivery, yard clean-up and removal.<br>
      <span class="services-extra">General maintenance and repairs.</span>
    </p>
  </section>

  <section class="card card--contact" aria-label="Contact side">
    <p class="contact-name">Brightway Haul &amp; Repair Services</p>
    <ul class="contact-list">
      <li class="contact-item">0419574302
        <svg class="contact-icon" viewBox="0 0 16 16" aria-hidden="true"><path d="M4 1h3l1 4-2 1c1 2 2 3 4 4l1-2 4 1v3c0 1-1 2-2 2C7 14 2 9 2 3c0-1 1-2 2-2z"/></svg>
      </li>
      <li class="contact-item">brightwayhaulrepair@mailbox.example
        <svg class="contact-icon" viewBox="0 0 16 16" aria-hidden="true"><path d="M1 3h14v10H1z M2 4l6 5 6-5" fill="none" stroke="var(--brand-blue-light)" stroke-width="1.5"/></svg>
      </li>
      <li class="contact-item contact-item--web">www.brightwayhaul.com.au
        <svg class="contact-icon" viewBox="0 0 16 16" aria-hidden="true"><circle cx="8" cy="8" r="6.5" fill="none" stroke="var(--brand-blue-light)" stroke-width="1.5"/><path d="M1.5 8h13M8 1.5c-3 3-3 10 0 13M8 1.5c3 3 3 10 0 13" fill="none" stroke="var(--brand-blue-light)" stroke-width="1.2"/></svg>
      </li>
    </ul>
    <div class="contact-stripe"></div>
  </section>

</main>
</body>
</html>
```